Business Card for Brevel Coatings

We need a simple, yet out standing business card for our painting company.

Target Market(s)

wealthy; high-end neighborhoods, and businesses

Industry/Entity Type

Painting

Contact Information for Business Card

Name:
Doran Vask

Email:
d.vask@brevel-coatings.com

Website:
Brevel-coatings.com

Phone Number:
(555) 416-9073

Font styles to use
Serif
Sans Serif

Requirements
Must have
• slogan "making change simple"
Should not have
• A title attached to the name on the card

```html
<!DOCTYPE html>
<html lang="en">
<head>
<meta charset="utf-8">
<title>Brevel Coatings – Business Card</title>
<link rel="stylesheet" href="https://fonts.googleapis.com/css2?family=Cinzel:wght@700&family=Arimo:wght@400;700&display=swap">
<style>
  :root {
    --forest: #3d5a10;
    --forest-deep: #34500c;
    --lime: #a9cf3a;
    --paper: #ffffff;
    --backdrop: #e9e7e1;
    --ink-light: #f2f5ea;
  }
  * { box-sizing: border-box; margin: 0; padding: 0; }
  html, body {
    width: 1200px; height: 950px; overflow: hidden;
    background: var(--backdrop);
    font-family: "Arimo", Arial, sans-serif;
  }
  .stage { position: relative; width: 1200px; height: 950px; }
  .card {
    position: absolute; left: 250px; width: 700px; height: 400px;
    overflow: hidden;
    box-shadow: 0 6px 18px rgba(0,0,0,.18);
  }
  .card-back { top: 60px; background: var(--forest); }
  .card-front { top: 490px; background: var(--paper); }

  .brand {
    display: flex; align-items: center; gap: 14px;
    font-family: "Cinzel", Georgia, serif; font-weight: 700;
    letter-spacing: 2px; white-space: nowrap;
  }
  .brand-mark { display: block; flex: none; }

  .card-back .brand {
    position: absolute; left: 0; right: 0; top: 140px;
    justify-content: center; color: var(--paper); font-size: 46px;
  }
  .card-back .brand-mark { width: 40px; height: 40px; background: var(--paper); }
  .slogan {
    position: absolute; left: 0; right: 0; top: 214px; text-align: center;
    color: var(--lime); font-size: 16px; letter-spacing: 4px; text-transform: uppercase;
  }
  .back-web {
    position: absolute; left: 0; right: 0; top: 282px; text-align: center;
    color: var(--ink-light); font-size: 15px; letter-spacing: 5px;
  }

  .front-shape { position: absolute; inset: 0; }
  .card-front .brand {
    position: absolute; right: 40px; top: 58px;
    color: var(--forest); font-size: 38px;
  }
  .card-front .brand-mark { width: 32px; height: 32px; background: var(--lime); }

  .contact {
    position: absolute; left: 40px; top: 124px; color: var(--paper);
  }
  .contact-name { font-size: 24px; font-weight: 700; }
  .contact-address { font-size: 15px; line-height: 22px; margin-top: 40px; }
  .contact-lines { list-style: none; margin-top: 24px; }
  .contact-lines li {
    display: flex; align-items: center; gap: 12px;
    font-size: 15px; height: 24px;
  }
  .contact-lines svg { width: 16px; height: 16px; flex: none; }
</style>
</head>
<body>
<main class="stage">

  <section class="card card-back" aria-label="Card back">
    <div class="brand"><span class="brand-mark"></span>BREVEL COATINGS</div>
    <p class="slogan">making change simple</p>
    <p class="back-web">www.brevel-coatings.com</p>
  </section>

  <section class="card card-front" aria-label="Card front">
    <svg class="front-shape" viewBox="0 0 700 400" width="700" height="400" aria-hidden="true">
      <path d="M0 0 H150 C250 200 500 270 700 205 V400 H0 Z" fill="var(--forest)"/>
      <path d="M260 238 C380 300 560 285 700 200 L700 212 C560 305 380 315 260 238 Z" fill="var(--lime)"/>
    </svg>

    <div class="brand"><span class="brand-mark"></span>BREVEL COATINGS</div>

    <div class="contact">
      <p class="contact-name">Doran Vask</p>
      <p class="contact-address">4127 Alder Crest Road<br>Lindmoor, NY 11990</p>
      <ul class="contact-lines">
        <li>
          <svg viewBox="0 0 16 16" fill="var(--paper)"><path d="M3 2 L6 2 L7 5 L5 6.5 C6 8.5 7.5 10 9.5 11 L11 9 L14 10 L14 13 C8 14 2 8 3 2 Z"/></svg>
          (555) 416-9073
        </li>
        <li>
          <svg viewBox="0 0 16 16" fill="none" stroke="var(--paper)" stroke-width="1.6"><rect x="4.5" y="1.5" width="7" height="13" rx="1"/><line x1="7" y1="12" x2="9" y2="12"/></svg>
          (555) 302-7718
        </li>
        <li>
          <svg viewBox="0 0 16 16" fill="var(--paper)"><rect x="4" y="1" width="8" height="5"/><rect x="1" y="6" width="14" height="6" rx="1"/><rect x="4" y="10" width="8" height="5"/></svg>
          (555) 284-6150
        </li>
        <li>
          <svg viewBox="0 0 16 16" fill="none" stroke="var(--paper)" stroke-width="1.6"><rect x="1.5" y="3.5" width="13" height="9"/><path d="M1.5 3.5 L8 9 L14.5 3.5"/></svg>
          d.vask@brevel-coatings.com
        </li>
        <li>
          <svg viewBox="0 0 16 16" fill="none" stroke="var(--paper)" stroke-width="1.4"><circle cx="8" cy="8" r="6.5"/><ellipse cx="8" cy="8" rx="3" ry="6.5"/><line x1="1.5" y1="8" x2="14.5" y2="8"/></svg>
          www.brevel-coatings.com
        </li>
      </ul>
    </div>
  </section>

</main>
</body>
</html>
```